Business card - Harbourline Stoneworks

Design a business card utilizing the given logo.
colors we like: Black, greys, Teal, blues.
Tri color card, horizontal orientation likely
Logo and name likely best on top.
Info on card:

Dennis Farrowby
#5 - 4180 Maple Ridge Blvd.
Surrey, B.C. V3K 2R9

778.555.0193
dennisfarrowby@brellnet.ca

Slogan: "Building Dreams"

We are a construction company that specializes in new home construction on the West coast of BC Canada. Open Concepts designs of high end homes.

```html
<!DOCTYPE html>
<html lang="en">
<head>
<meta charset="utf-8">
<title>Harbourline Stoneworks – Business Card</title>
<link rel="stylesheet" href="https://fonts.googleapis.com/css2?family=Source+Sans+3:wght@400;700&display=swap">
<style>
  :root {
    --sky-blue: #00aeef;
    --deep-blue: #1b78c0;
    --slate: #252f3a;
    --band-grey: #bcbec0;
    --ink-black: #111417;
    --text-light: #d3d7dc;
    --divider-grey: #b9bcc0;
  }
  html, body {
    margin: 0;
    padding: 0;
    width: 1200px;
    height: 685px;
    overflow: hidden;
    background: var(--sky-blue);
  }
  .business-card {
    position: relative;
    width: 1200px;
    height: 685px;
    overflow: hidden;
    background: var(--sky-blue);
    font-family: "Source Sans 3", "Myriad Pro", Arial, sans-serif;
  }
  .card-shapes {
    position: absolute;
    inset: 0;
  }
  .brand {
    position: absolute;
    left: 50px;
    top: 62px;
    display: flex;
    align-items: center;
    gap: 22px;
  }
  .brand-dot {
    width: 100px;
    height: 100px;
    border-radius: 50%;
    background: var(--ink-black);
  }
  .brand-name {
    font-weight: 700;
    font-size: 54px;
    line-height: 1;
    color: var(--ink-black);
    letter-spacing: 0.5px;
  }
  .person {
    position: absolute;
    left: 50px;
    top: 476px;
  }
  .person-name {
    margin: 0;
    font-weight: 700;
    font-size: 50px;
    line-height: 1;
    color: var(--sky-blue);
    letter-spacing: 0.3px;
  }
  .slogan {
    margin: 8px 0 0;
    font-weight: 400;
    font-size: 32px;
    line-height: 1;
    color: var(--text-light);
  }
  .contact-divider {
    position: absolute;
    left: 581px;
    top: 400px;
    width: 9px;
    height: 195px;
    background: var(--divider-grey);
  }
  .contact-list {
    position: absolute;
    left: 634px;
    top: 398px;
    margin: 0;
    padding: 0;
    list-style: none;
    color: var(--text-light);
    font-size: 28px;
    line-height: 1.15;
  }
  .contact-item {
    display: flex;
    align-items: flex-start;
    gap: 16px;
  }
  .contact-item + .contact-item { margin-top: 22px; }
  .contact-icon {
    flex: none;
    width: 34px;
    height: 34px;
    fill: var(--sky-blue);
    margin-top: 2px;
  }
  .contact-item--email .contact-icon { margin-top: 4px; }
</style>
</head>
<body>
  <div class="business-card">
    <svg class="card-shapes" width="1200" height="685" viewBox="0 0 1200 685" aria-hidden="true">
      <polygon class="accent-stripe" points="500,293 1153,37 1200,433 1138,58" fill="var(--deep-blue)"/>
      <polygon class="slate-panel" points="0,447 1138,58 1200,433 1200,607 0,607" fill="var(--slate)"/>
      <rect class="footer-band" x="0" y="607" width="1200" height="78" fill="var(--band-grey)"/>
    </svg>

    <header class="brand">
      <div class="brand-dot"></div>
      <div class="brand-name">Harbourline Stoneworks</div>
    </header>

    <section class="person">
      <h1 class="person-name">DENNIS FARROWBY</h1>
      <p class="slogan">Building Dreams</p>
    </section>

    <div class="contact-divider"></div>

    <ul class="contact-list">
      <li class="contact-item contact-item--address">
        <svg class="contact-icon" viewBox="0 0 24 24" aria-hidden="true"><path d="M12 1.5a7.5 7.5 0 0 0-7.5 7.5c0 5.6 7.5 13.5 7.5 13.5s7.5-7.9 7.5-13.5A7.5 7.5 0 0 0 12 1.5zm0 10.5a3 3 0 1 1 0-6 3 3 0 0 1 0 6z"/></svg>
        <span>#5 - 4180 Maple Ridge Blvd.<br>Surrey, B.C. V3K 2R9</span>
      </li>
      <li class="contact-item contact-item--email">
        <svg class="contact-icon" viewBox="0 0 24 24" aria-hidden="true"><path d="M2 5h20v14H2z M3.5 6.5v.6l8.5 6 8.5-6v-.6z" fill-rule="evenodd"/></svg>
        <span>dennisfarrowby@brellnet.ca</span>
      </li>
      <li class="contact-item contact-item--phone">
        <svg class="contact-icon" viewBox="0 0 24 24" aria-hidden="true"><path d="M6.6 10.8a15.1 15.1 0 0 0 6.6 6.6l2.2-2.2a1 1 0 0 1 1-.25 11.4 11.4 0 0 0 3.6.57 1 1 0 0 1 1 1V20a1 1 0 0 1-1 1A17 17 0 0 1 3 4a1 1 0 0 1 1-1h3.5a1 1 0 0 1 1 1c0 1.25.2 2.45.57 3.57a1 1 0 0 1-.25 1z"/></svg>
        <span>778.555.0193</span>
      </li>
    </ul>
  </div>
</body>
</html>
```